Business Card for Bright Lantern

Please design a Modern Business card for a Online Marketing Company

Website: http://www.brightlantern-example.com.au

Please do NOT include physical address in design.

Industry/Entity Type

Business

```html
<!DOCTYPE html>
<html lang="en">
<head>
<meta charset="utf-8">
<title>Bright Lantern – Business Card</title>
<link rel="stylesheet" href="https://fonts.googleapis.com/css2?family=Exo+2:wght@200&family=Open+Sans:wght@400&family=Russo+One&display=swap">
<style>
  :root {
    --maroon: #8c1726;
    --red: #b51f32;
    --blush: #e8d0c7;
    --white: #ffffff;
    --card-edge: #a03a48;
    --stage-light: #ffffff;
    --stage-edge: #dcdddd;
    --label: #111111;
  }
  html, body {
    margin: 0;
    padding: 0;
    overflow: hidden;
  }
  .stage {
    position: relative;
    width: 1200px;
    height: 1000px;
    overflow: hidden;
    background: radial-gradient(ellipse 620px 560px at 600px 520px, var(--stage-light) 0%, #f3f3f3 55%, var(--stage-edge) 100%);
  }
  .side-label {
    position: absolute;
    left: 153px;
    margin: 0;
    font-family: "Russo One", sans-serif;
    font-size: 40px;
    line-height: 1;
    color: var(--label);
    letter-spacing: 1px;
  }
  .side-label--front { top: 310px; }
  .side-label--back { top: 718px; letter-spacing: 3px; }

  .card {
    position: absolute;
    box-sizing: border-box;
    width: 605px;
    height: 291px;
  }
  .card--front {
    left: 313px;
    top: 189px;
    background: var(--maroon);
  }
  .card--back {
    left: 315px;
    top: 577px;
    background: var(--white);
    border: 1px solid var(--card-edge);
  }

  .front-name {
    position: absolute;
    left: 0;
    right: 0;
    top: 118px;
    display: flex;
    justify-content: center;
    align-items: center;
    gap: 16px;
  }
  .front-name__mark {
    width: 30px;
    height: 30px;
    background: var(--blush);
  }
  .front-name__text {
    font-family: "Exo 2", sans-serif;
    font-weight: 200;
    font-size: 46px;
    line-height: 1;
    color: var(--blush);
  }

  .brand {
    position: absolute;
    left: 30px;
    top: 96px;
    display: flex;
    align-items: center;
    gap: 58px;
  }
  .brand__mark {
    width: 44px;
    height: 44px;
    background: var(--red);
  }
  .brand__name {
    font-family: "Exo 2", sans-serif;
    font-weight: 200;
    font-size: 44px;
    line-height: 1;
    color: var(--maroon);
  }
  .tagline {
    position: absolute;
    left: 200px;
    top: 153px;
    margin: 0;
    font-family: "Open Sans", sans-serif;
    font-size: 19px;
    line-height: 1.3;
    color: var(--maroon);
    white-space: nowrap;
  }
  .web-band {
    position: absolute;
    right: 0;
    bottom: 0;
    width: 305px;
    height: 45px;
  }
  .web-band svg {
    position: absolute;
    inset: 0;
  }
  .web-band__url {
    position: absolute;
    left: 64px;
    top: 13px;
    font-family: "Open Sans", sans-serif;
    font-size: 13.5px;
    color: var(--white);
    white-space: nowrap;
  }
</style>
</head>
<body>
  <main class="stage">
    <p class="side-label side-label--front">FRONT</p>
    <section class="card card--front" aria-label="Card front">
      <div class="front-name">
        <span class="front-name__mark" aria-hidden="true"></span>
        <span class="front-name__text">Bright Lantern</span>
      </div>
    </section>

    <p class="side-label side-label--back">BACK</p>
    <section class="card card--back" aria-label="Card back">
      <div class="brand">
        <span class="brand__mark" aria-hidden="true"></span>
        <span class="brand__name">Bright Lantern</span>
      </div>
      <p class="tagline">Get seen online -grow online</p>
      <div class="web-band">
        <svg width="305" height="45" viewBox="0 0 305 45" aria-hidden="true">
          <polygon points="0,45 60,0 305,0 305,45" fill="var(--maroon)"/>
        </svg>
        <span class="web-band__url">www.brightlantern-example.com.au</span>
      </div>
    </section>
  </main>
</body>
</html>
```